New Consulting Firm News PowerPoint Template

We are a new consulting firm that specializes in Veltrix Unified Planning Suite implementations in need of a new PowerPoint template. We need at least the following layouts:
• Main Cover Slide
• Agenda / Table of Contents
• Title slide for each of the agenda items leading into actual content
• Title + Content with nice bullets in the content
• Title + Sub-Title + Content with nice bullets in the content
• Title + Two Columns of Content
• Title + Sub-Title + Two Columns of Content
• Title + Three Columns of Content
• Title + Sub-Title + Three Columns of Content
• Title + Two Rows and Two Columns of Content (4 boxes)
• Title + Sub-Title + Two Rows and Two Columns of Content (4 boxes)
• Title + Blank
• Nascar Slide (Client logos arranged somehow)
• Case Study Slide
• Various infographic slides than can be used and modified would be amazing as well
Our logo has been uploaded and you can find our website here:
https://brannowadvisory.com
We would like the main theme colors to blend with our logo, but also have a variety of colors in the theme that compliment the main theme colors. Once we have selected a PowerPoint design we expect to immediately have a Word design contest and the winning PowerPoint design will likely be a heavy influence on the Word design.

Target Market(s)

CFO, CAO, VP of Finance, Controllers

Industry/Entity Type

Consulting

Font styles to use
Serif
Sans Serif

Requirements
Must have
• • Main Cover Slide
• Title + Blank
• Case Study Slide
Nice to have
• • Various infographic slides than can be used and modified would be amazing as well

```html
<!DOCTYPE html>
<html lang="en">
<head>
<meta charset="utf-8">
<title>Brannow Advisory – Presentation Template</title>
<link href="https://fonts.googleapis.com/css2?family=Montserrat:wght@400;500;600;700;800&display=swap" rel="stylesheet">
<style>
:root{
  --blue:#1f74c7;
  --blue-light:#3d96f0;
  --slate:#5b5e62;
  --charcoal:#3a3b3e;
  --ink:#1d1d1f;
  --mid:#a7a8aa;
  --pale:#e4e4e5;
  --text:#6b6c6f;
  --white:#ffffff;
}
*{margin:0;padding:0;box-sizing:border-box}
html,body{width:1200px;height:2194px;overflow:hidden;background:#e6e6e7}
body{font-family:"Montserrat",sans-serif;color:var(--text)}
.stage{position:absolute;left:0;top:0;width:1409px;height:2576px;transform:scale(.85167);transform-origin:0 0;
  background:linear-gradient(180deg,#ececed 0%,#e2e2e3 40%,#dcdcdd 100%)}

/* brand */
.brand{position:absolute;left:0;top:255px;width:1409px;display:flex;justify-content:center;align-items:center;gap:16px}
.brand-square{width:34px;height:34px;background:var(--blue)}
.brand-name{font-size:40px;font-weight:600;letter-spacing:3px;color:var(--blue)}

/* slides */
.slide{position:absolute;width:424px;height:238px;background:var(--white);overflow:hidden;box-shadow:0 10px 22px rgba(0,0,0,.22)}
.abs{position:absolute}
.panel{position:absolute;top:11px;height:216px;background:var(--slate)}
.panel.dark{background:var(--charcoal)}
.panel.grey{background:var(--mid)}
.mark{position:absolute;display:flex;align-items:center;gap:2px;font-size:4px;font-weight:700;letter-spacing:.3px;color:var(--blue)}
.mark i{display:block;width:6px;height:6px;background:var(--blue)}
.mark.light{color:var(--white)}
.mark.light i{background:var(--white)}
.head{position:absolute}
.ttl{font-size:10.5px;font-weight:700;line-height:1.12;text-transform:uppercase;color:var(--white)}
.ttl.ink{color:var(--ink)}
.dash{width:12px;height:1.6px;background:var(--white);margin:7px 0 5px}
.dash.ink{background:var(--ink)}
.lorem{font-size:4.2px;line-height:1.55;color:#d9d9da;text-align:justify}
.lorem.ink{color:var(--text)}
.foot{position:absolute;left:28px;right:18px;bottom:3px;display:flex;font-size:2.8px;color:#777;font-weight:600}
.foot span:nth-child(1){width:172px}
.foot span:nth-child(2){flex:1}
.item{position:absolute;display:flex;gap:9px;width:150px}
.pill{flex:none;width:6px;height:13px;border-radius:3px;background:var(--blue);position:relative;margin-top:1px}
.pill::after{content:"";position:absolute;left:2.5px;top:3px;width:1px;height:7px;background:var(--white)}
.pill.white{background:var(--white)}
.pill.white::after{background:var(--slate)}
.item h4{font-size:4.6px;font-weight:500;color:var(--text);letter-spacing:.2px;margin-bottom:1.5px}
.item p{font-size:3.9px;line-height:1.5;color:var(--text)}
.on-dark h4{color:#e4e4e4}
.on-dark p{color:#d0d0d0}
.cols{position:absolute;display:flex;gap:12px}
.cols p{font-size:3.9px;line-height:1.55;color:#e1e1e1;text-align:justify}
.cols p+p{margin-top:5px}
.agenda{position:absolute;left:215px;top:35px;width:180px;list-style:none}
.agenda li{display:flex;gap:7px;font-size:4.1px;font-weight:600;color:#7b7c7f;line-height:1.45;margin-bottom:3.4px;letter-spacing:.2px}
.agenda b{color:var(--blue);width:9px;flex:none}
.num{position:absolute;font-size:11px;font-weight:600;color:var(--white)}
.table-head{position:absolute;display:flex;background:var(--blue)}
.table-head div{flex:1;display:flex;align-items:center;justify-content:center;font-size:4.3px;font-weight:600;color:var(--white);border-right:1px solid #4f93d6}
.table-rows{position:absolute;display:flex;flex-direction:column;background:#8d8e91}
.table-rows div{flex:1;display:flex;align-items:center;padding-left:9px;font-size:4.3px;font-weight:600;color:var(--white);border-bottom:1px solid #a9aaad}
.table-body{position:absolute;background:#dcdcdd;display:grid;grid-template-columns:1fr 1fr;grid-template-rows:1fr 1fr;gap:1px}
.table-body div{background:#dcdcdd;outline:1px solid #cfcfd0}
.feat{position:absolute;width:70px;text-align:center}
.feat svg{display:block;margin:0 auto 3px}
.feat h4{font-size:4.4px;font-weight:500;color:#d8d8d8;margin-bottom:2px}
.feat p{font-size:3.6px;line-height:1.45;color:#c9c9c9}
.nascar{position:absolute;font-size:7px;font-weight:700;letter-spacing:.5px;text-align:center;width:70px}
.nascar.a{color:var(--slate)}
.nascar.b{color:var(--blue)}
.flow{position:absolute;border-radius:3px;padding:4px 6px;font-size:4.2px;line-height:1.45;color:var(--white)}
.flow b{display:block;font-size:4.6px}
.photo{position:absolute;background:linear-gradient(135deg,#e9eef1 0%,#c9d2d6 35%,#8c9499 55%,#dfe0dc 75%,#b7b3ab 100%)}
.pattern{position:absolute;background:linear-gradient(135deg,#f6f6f6 0%,#ececec 45%,#f7f7f7 60%,#e3e3e3 100%)}
</style>
</head>
<body>
<div class="stage">

  <div class="brand"><span class="brand-square"></span><span class="brand-name">BRANNOW ADVISORY</span></div>

  <!-- 1 cover -->
  <section class="slide" style="left:22px;top:430px">
    <div class="pattern" style="inset:0" role="img" aria-label="Soft white geometric tiles background"></div>
    <div class="abs" style="left:24px;top:103px;display:flex;align-items:center;gap:5px">
      <span style="width:11px;height:11px;background:var(--blue)"></span>
      <span style="font-size:13px;font-weight:600;color:var(--blue);letter-spacing:.5px">BRANNOW</span>
    </div>
    <div class="abs" style="left:150px;top:96px;width:245px;text-align:center">
      <div style="font-size:13.5px;font-weight:400;color:#55575b;line-height:1.15">YOU CAN PLACE YOUR TITLE<br>PRESENTATION HERE</div>
      <div style="font-size:4.2px;font-weight:700;color:#55575b;margin-top:6px;letter-spacing:.3px">YOUR SUBTITLE PRESENTATION TITLE GOES HERE</div>
      <div style="font-size:4.2px;font-weight:600;color:#55575b;margin-top:20px">MARCH, 20 2021</div>
    </div>
  </section>

  <!-- 2 agenda -->
  <section class="slide" style="left:492px;top:430px">
    <div class="panel" style="left:11px;width:185px"></div>
    <div class="mark light" style="left:30px;top:27px"><i></i>BRANNOW</div>
    <div class="head" style="left:30px;top:115px;width:150px">
      <div class="ttl">Title content<br>with bullets in<br>the content</div><div class="dash"></div>
      <p class="lorem">Lorem ipsum sit lom dolor sit amet, consectetur sit amet adipiscing. Lorem ipsum sit lom dolor. Lorem ipsum.</p>
    </div>
    <ol class="agenda">
      <li><b>01.</b>TITLE + CONTENT WITH NICE BULLETS IN THE CONTENT</li>
      <li><b>02.</b>TITLE + SUB-TITLE + CONTENT WITH NICE BULLETS IN THE CONTENT</li>
      <li><b>03.</b>TITLE + TWO COLUMNS OF CONTENT</li>
      <li><b>04.</b>TITLE + SUB-TITLE + TWO COLUMNS OF CONTENT</li>
      <li><b>05.</b>TITLE + SUB-TITLE + THREE COLUMNS OF CONTENT</li>
      <li><b>06.</b>TITLE + THREE COLUMNS OF CONTENT</li>
      <li><b>07.</b>TITLE + SUB-TITLE + THREE COLUMNS OF CONTENT</li>
      <li><b>08.</b>TITLE + TWO ROWS AND TWO COLUMNS OF CONTENT (4 BOXES)</li>
      <li><b>09.</b>TITLE + SUB-TITLE + TWO ROWS AND TWO COLUMNS OF CONTENT (4 BOXES)</li>
      <li><b>10.</b>TITLE + BLANK</li>
      <li><b>11.</b>NASCAR SLIDE (CLIENT LOGOS)</li>
      <li><b>12.</b>CASE STUDY SLIDE</li>
      <li><b>13.</b>DATA TABLES</li>
      <li><b>14.</b>EDITABLE INFOGRAPHIC SLIDES</li>
    </ol>
    <div class="foot"><span>www.brannowadvisory.com</span><span>CONFIDENTIAL</span><span>1</span></div>
  </section>

  <!-- 3 bullets -->
  <section class="slide" style="left:962px;top:430px">
    <div class="panel" style="left:11px;width:185px"></div>
    <div class="mark light" style="left:30px;top:27px"><i></i>BRANNOW</div>
    <div class="head" style="left:30px;top:115px;width:150px">
      <div class="ttl">Title content<br>with bullets in<br>the content</div><div class="dash"></div>
      <p class="lorem">Lorem ipsum sit lom dolor sit amet, consectetur sit amet adipiscing. Lorem ipsum sit lom dolor. Lorem ipsum.</p>
    </div>
    <div class="item" style="left:245px;top:32px"><span class="pill"></span><div><h4>INSERT TITLE HERE</h4><p>Lorem ipsum sit lom dolor sit amet,<br>consectetur sit amet. Lorem.</p></div></div>
    <div class="item" style="left:245px;top:82px"><span class="pill"></span><div><h4>INSERT TITLE HERE</h4><p>Lorem ipsum sit lom dolor sit amet,<br>consectetur sit amet. Lorem.</p></div></div>
    <div class="item" style="left:245px;top:133px"><span class="pill"></span><div><h4>INSERT TITLE HERE</h4><p>Lorem ipsum sit lom dolor sit amet,<br>consectetur sit amet. Lorem.</p></div></div>
    <div class="item" style="left:245px;top:183px"><span class="pill"></span><div><h4>INSERT TITLE HERE</h4><p>Lorem ipsum sit lom dolor sit amet,<br>consectetur sit amet. Lorem.</p></div></div>
    <div class="foot"><span>www.brannowadvisory.com</span><span>CONFIDENTIAL</span><span>2</span></div>
  </section>

  <!-- 4 -->
  <section class="slide" style="left:22px;top:726px">
    <div class="mark" style="left:30px;top:27px"><i></i>BRANNOW</div>
    <div class="head" style="left:30px;top:115px;width:120px">
      <div class="ttl ink">Title content<br>with bullets in<br>the content</div><div class="dash ink"></div>
      <p class="lorem ink">Lorem ipsum sit lom dolor sit amet, consectetur sit amet adipiscing. Lorem ipsum sit lom dolor. Lorem ipsum.</p>
    </div>
    <div class="panel" style="left:183px;width:230px"></div>
    <div class="item on-dark" style="left:245px;top:57px"><span class="pill white"></span><div><h4>INSERT TITLE HERE</h4><p>Lorem ipsum sit lom dolor sit amet,<br>consectetur sit amet. Lorem.</p></div></div>
    <div class="item on-dark" style="left:245px;top:114px"><span class="pill white"></span><div><h4>INSERT TITLE HERE</h4><p>Lorem ipsum sit lom dolor sit amet,<br>consectetur sit amet. Lorem.</p></div></div>
    <div class="item on-dark" style="left:245px;top:171px"><span class="pill white"></span><div><h4>INSERT TITLE HERE</h4><p>Lorem ipsum sit lom dolor sit amet,<br>consectetur sit amet. Lorem.</p></div></div>
    <div class="foot"><span>www.brannowadvisory.com</span><span>CONFIDENTIAL</span><span>3</span></div>
  </section>

  <!-- 5 -->
  <section class="slide" style="left:492px;top:726px">
    <div class="panel" style="left:11px;width:177px"></div>
    <div class="mark light" style="left:30px;top:27px"><i></i>BRANNOW</div>
    <div class="head" style="left:30px;top:103px;width:145px">
      <div class="ttl">Title content<br>with bullets in<br>the content &amp;<br>subtitle</div><div class="dash"></div>
      <p class="lorem">Lorem ipsum sit lom dolor sit amet, consectetur sit amet adipiscing. Lorem ipsum sit lom dolor. Lorem ipsum.</p>
    </div>
    <div class="item" style="left:212px;top:32px;width:95px"><span class="pill"></span><div><h4>INSERT TITLE HERE</h4><p>Lorem ipsum sit lom dolor sit amet, consectetur sit amet. Lorem.</p></div></div>
    <div class="item" style="left:315px;top:32px;width:95px"><span class="pill"></span><div><h4>INSERT TITLE HERE</h4><p>Lorem ipsum sit lom dolor sit amet, consectetur sit amet. Lorem.</p></div></div>
    <div class="item" style="left:212px;top:99px;width:95px"><span class="pill"></span><div><h4>INSERT TITLE HERE</h4><p>Lorem ipsum sit lom dolor sit amet, consectetur sit amet. Lorem.</p></div></div>
    <div class="item" style="left:315px;top:99px;width:95px"><span class="pill"></span><div><h4>INSERT TITLE HERE</h4><p>Lorem ipsum sit lom dolor sit amet, consectetur sit amet. Lorem.</p></div></div>
    <div class="item" style="left:212px;top:166px;width:95px"><span class="pill"></span><div><h4>INSERT TITLE HERE</h4><p>Lorem ipsum sit lom dolor sit amet, consectetur sit amet. Lorem.</p></div></div>
    <div class="item" style="left:315px;top:166px;width:95px"><span class="pill"></span><div><h4>INSERT TITLE HERE</h4><p>Lorem ipsum sit lom dolor sit amet, consectetur sit amet. Lorem.</p></div></div>
    <div class="foot"><span>www.brannowadvisory.com</span><span>CONFIDENTIAL</span><span>4</span></div>
  </section>

  <!-- 6 -->
  <section class="slide" style="left:962px;top:726px">
    <div class="mark" style="left:30px;top:27px"><i></i>BRANNOW</div>
    <div class="head" style="left:30px;top:103px;width:145px">
      <div class="ttl ink">Title content<br>with bullets in<br>the content &amp;<br>subtitle</div><div class="dash ink"></div>
      <p class="lorem ink">Lorem ipsum sit lom dolor sit amet, consectetur sit amet adipiscing. Lorem ipsum sit lom dolor. Lorem ipsum.</p>
    </div>
    <div class="panel" style="left:184px;width:229px"></div>
    <div class="item on-dark" style="left:202px;top:32px;width:95px"><span class="pill"></span><div><h4>INSERT TITLE HERE</h4><p>Lorem ipsum sit lom dolor sit amet, consectetur sit amet. Lorem.</p></div></div>
    <div class="item on-dark" style="left:305px;top:32px;width:95px"><span class="pill"></span><div><h4>INSERT TITLE HERE</h4><p>Lorem ipsum sit lom dolor sit amet, consectetur sit amet. Lorem.</p></div></div>
    <div class="item on-dark" style="left:202px;top:99px;width:95px"><span class="pill"></span><div><h4>INSERT TITLE HERE</h4><p>Lorem ipsum sit lom dolor sit amet, consectetur sit amet. Lorem.</p></div></div>
    <div class="item on-dark" style="left:305px;top:99px;width:95px"><span class="pill"></span><div><h4>INSERT TITLE HERE</h4><p>Lorem ipsum sit lom dolor sit amet, consectetur sit amet. Lorem.</p></div></div>
    <div class="item on-dark" style="left:202px;top:166px;width:95px"><span class="pill"></span><div><h4>INSERT TITLE HERE</h4><p>Lorem ipsum sit lom dolor sit amet, consectetur sit amet. Lorem.</p></div></div>
    <div class="item on-dark" style="left:305px;top:166px;width:95px"><span class="pill"></span><div><h4>INSERT TITLE HERE</h4><p>Lorem ipsum sit lom dolor sit amet, consectetur sit amet. Lorem.</p></div></div>
    <div class="foot"><span>www.brannowadvisory.com</span><span>CONFIDENTIAL</span><span>5</span></div>
  </section>

  <!-- 7 -->
  <section class="slide" style="left:22px;top:1022px">
    <div class="mark" style="left:30px;top:27px"><i></i>BRANNOW</div>
    <div class="head" style="left:30px;top:96px;width:100px">
      <div class="ttl ink">Title<br>columns<br>content<br>(w/bullet<br>simple text)</div><div class="dash ink"></div>
      <p class="lorem ink">Lorem ipsum sit lom dolor sit amet, consectetur sit amet adipiscing. Lorem ipsum sit lom dolor. Lorem ipsum.</p>
    </div>
    <div class="panel" style="left:149px;width:264px"></div>
    <div class="cols" style="left:168px;top:29px;width:105px">
      <div><p>Lorem ipsum dolor sit amet, consectetur adipiscing elit, sed do eiusmod tempor incididunt ut labore et dolore magna aliqua. Ut enim ad minim veniam. Quis nostrud exercitation ullamco laboris nisi ut aliquip ex ea commodo consequat. Duis aute irure dolor in reprehenderit in voluptate velit.</p>
      <p>Lorem ipsum dolor sit amet, consectetur adipiscing elit, sed do eiusmod tempor incididunt ut labore. Lorem ipsum dolor sit amet, consectetur adipiscing elit, sed do eiusmod tempor incididunt ut labore et dolore magna aliqua. Ut enim ado. Lorem ipsum dolor sit amet, consectetur adipiscing elit, sed do eiusmod tempor incididunt ut labore.</p></div>
    </div>
    <div class="item on-dark" style="left:283px;top:55px;width:125px"><span class="pill"></span><div><h4>INSERT TITLE HERE</h4><p>Lorem ipsum sit lom dolor sit amet, consectetur sit amet. Lorem.</p></div></div>
    <div class="item on-dark" style="left:283px;top:112px;width:125px"><span class="pill"></span><div><h4>INSERT TITLE HERE</h4><p>Lorem ipsum sit lom dolor sit amet, consectetur sit amet. Lorem.</p></div></div>
    <div class="item on-dark" style="left:283px;top:170px;width:125px"><span class="pill"></span><div><h4>INSERT TITLE HERE</h4><p>Lorem ipsum sit lom dolor sit amet, consectetur sit amet. Lorem.</p></div></div>
    <div class="foot"><span>www.brannowadvisory.com</span><span>CONFIDENTIAL</span><span>6</span></div>
  </section>

  <!-- 8 -->
  <section class="slide" style="left:492px;top:1022px">
    <div class="mark" style="left:30px;top:27px"><i></i>BRANNOW</div>
    <div class="head" style="left:30px;top:120px;width:110px">
      <div class="ttl ink">Title two<br>columns<br>content</div><div class="dash ink"></div>
      <p class="lorem ink">Lorem ipsum sit lom dolor sit amet, consectetur sit amet adipiscing. Lorem ipsum sit lom dolor. Lorem ipsum.</p>
    </div>
    <div class="panel" style="left:149px;width:264px"></div>
    <div class="cols" style="left:168px;top:40px;width:227px">
      <div style="flex:1"><p>Lorem ipsum dolor sit amet, consectetur adipiscing elit, sed do eiusmod tempor incididunt ut labore et dolore magna aliqua. Ut enim ad minim veniam. Quis nostrud exercitation ullamco laboris nisi ut aliquip ex ea commodo consequat. Duis aute irure dolor in reprehenderit in voluptate velit.</p>
      <p>Lorem ipsum dolor sit amet, consectetur adipiscing elit, sed do eiusmod tempor incididunt ut labore. Lorem ipsum dolor sit amet, consectetur adipiscing elit, sed do eiusmod tempor incididunt ut labore et dolore magna aliqua. Ut enim ado. Lorem ipsum dolor sit amet, consectetur adipiscing elit, sed do eiusmod tempor incididunt ut labore.</p></div>
      <div style="flex:1"><p>Lorem ipsum dolor sit amet, consectetur adipiscing elit, sed do eiusmod tempor incididunt ut labore et dolore magna aliqua. Ut enim ad minim veniam.</p>
      <p>Quis nostrud exercitation ullamco laboris nisi ut aliquip ex ea commodo consequat. Duis aute irure dolor in reprehenderit in voluptate velit.</p>
      <p>Lorem ipsum dolor sit amet, consectetur adipiscing elit, sed do eiusmod tempor incididunt ut labore. Lorem ipsum dolor sit amet, consectetur adipiscing elit, sed do eiusmod tempor incididunt ut labore et dolore magna aliqua. Ut enim ado.</p></div>
    </div>
    <div class="foot"><span>www.brannowadvisory.com</span><span>CONFIDENTIAL</span><span>7</span></div>
  </section>

  <!-- 9 -->
  <section class="slide" style="left:962px;top:1022px">
    <div class="mark" style="left:30px;top:27px"><i></i>BRANNOW</div>
    <div class="head" style="left:30px;top:108px;width:95px">
      <div class="ttl ink">Title +<br>three<br>columns of<br>content</div><div class="dash ink"></div>
      <p class="lorem ink">Lorem ipsum sit lom dolor sit amet, consectetur sit amet adipiscing. Lorem ipsum sit lom dolor. Lorem ipsum.</p>
    </div>
    <div class="panel" style="left:132px;width:281px"></div>
    <div class="cols" style="left:152px;top:48px;width:243px">
      <div style="flex:1"><p>Lorem ipsum dolor sit amet, consectetur adipiscing elit, sed do eiusmod tempor incididunt ut labore et dolore magna aliqua. Ut enim ad minim veniam. Quis nostrud exercitation ullamco laboris nisi ut aliquip ex ea commodo consequat.</p><p>Duis aute irure dolor in reprehenderit in voluptate velit. Lorem ipsum dolor sit amet, consectetur adipiscing elit, sed do eiusmod tempor incididunt ut labore lorem.</p></div>
      <div style="flex:1"><p>Lorem ipsum dolor sit amet, consectetur adipiscing elit, sed do eiusmod tempor incididunt ut labore et dolore magna aliqua. Ut enim ad minim veniam. Quis nostrud exercitation ullamco laboris nisi ut aliquip ex ea commodo consequat. Duis aute irure dolor in reprehenderit in voluptate velit.</p><p>Lorem ipsum dolor sit amet, consectetur adipiscing elit, sed do eiusmod tempor incididunt ut labore lorem.</p></div>
      <div style="flex:1"><p>Lorem ipsum dolor sit amet, consectetur adipiscing elit, sed do eiusmod tempor incididunt ut labore et dolore magna aliqua. Ut enim ad minim veniam.</p><p>Quis nostrud exercitation ullamco laboris nisi ut aliquip ex ea commodo consequat. Duis aute irure dolor in reprehenderit in voluptate velit. Lorem ipsum dolor sit amet, consectetur adipiscing elit, sed do eiusmod.</p></div>
    </div>
    <div class="foot"><span>www.brannowadvisory.com</span><span>CONFIDENTIAL</span><span>8</span></div>
  </section>

  <!-- 10 four points -->
  <section class="slide" style="left:22px;top:1319px">
    <svg class="abs" style="left:0;top:0" width="424" height="238">
      <polygon points="11,11 240,11 180,227 11,227" fill="#5b5e62"/>
      <polygon points="240,11 282,11 222,227 180,227" fill="#a7a8aa"/>
    </svg>
    <div class="mark light" style="left:30px;top:27px"><i></i>BRANNOW</div>
    <div class="head" style="left:30px;top:85px;width:130px">
      <div class="ttl">Four points<br>features w/<br>icons</div><div class="dash"></div>
      <p class="lorem">Lorem ipsum sit lom dolor sit amet, consectetur sit amet adipiscing. Lorem ipsum sit lom dolor. Lorem ipsum.</p>
      <p class="lorem" style="margin-top:5px">Lorem ipsum sit lom dolor sit amet, consectetur sit amet adipiscing. Lorem ipsum sit lom dolor. Lorem ipsum.</p>
    </div>
    <span class="num" style="left:243px;top:53px">1</span>
    <span class="num" style="left:230px;top:92px">2</span>
    <span class="num" style="left:217px;top:131px">3</span>
    <span class="num" style="left:203px;top:170px">4</span>
    <div class="item" style="left:293px;top:53px;width:110px;display:block"><h4>INSERT TITLE HERE</h4><p>Lorem ipsum sit lom dolor sit amet, consectetur sit amet.</p></div>
    <div class="item" style="left:281px;top:92px;width:120px;display:block"><h4>INSERT TITLE HERE</h4><p>Lorem ipsum sit lom dolor sit amet, consectetur sit amet.</p></div>
    <div class="item" style="left:268px;top:131px;width:130px;display:block"><h4>INSERT TITLE HERE</h4><p>Lorem ipsum sit lom dolor sit amet, consectetur sit amet.</p></div>
    <div class="item" style="left:257px;top:170px;width:140px;display:block"><h4>INSERT TITLE HERE</h4><p>Lorem ipsum sit lom dolor sit amet, consectetur sit amet. Lorem ipsum sit lom dolor sit amet, consectetur sit amet.</p></div>
    <div class="foot"><span>www.brannowadvisory.com</span><span>CONFIDENTIAL</span><span>9</span></div>
  </section>

  <!-- 11 multiple info -->
  <section class="slide" style="left:492px;top:1319px">
    <div class="pattern" style="inset:0" role="img" aria-label="Soft grey geometric tiles background"></div>
    <svg class="abs" style="left:0;top:0" width="424" height="238">
      <polygon points="0,17 330,17 270,217 0,217" fill="#3a3b3e"/>
      <g fill="#fff" stroke="#cfcfd0" stroke-width="1.5">
        <circle cx="312" cy="80" r="10"/><circle cx="298" cy="123" r="10"/><circle cx="285" cy="166" r="10"/>
      </g>
      <g fill="#5b5e62">
        <rect x="307" y="75" width="10" height="7" rx="1"/><rect x="311" y="82" width="2" height="3"/>
        <path d="M298 118 A5 5 0 1 0 303 123 L298 123 Z"/>
        <rect x="280" y="161" width="10" height="8" rx="1"/>
      </g>
    </svg>
    <div class="mark light" style="left:30px;top:27px"><i></i>BRANNOW</div>
    <div class="head" style="left:30px;top:60px;width:90px">
      <div class="ttl">Multiple<br>info slide</div><div class="dash"></div>
      <p class="lorem">Lorem ipsum sit lom dolor sit amet, consectetur sit amet adipiscing.</p>
      <p class="lorem" style="margin-top:5px">Lorem ipsum sit lom dolor sit amet, consectetur sit amet adipiscing.</p>
      <p class="lorem" style="margin-top:5px">Lorem ipsum sit lom dolor sit amet, consectetur sit amet adipiscing.</p>
    </div>
    <span class="num" style="left:137px;top:58px">1</span>
    <span class="num" style="left:137px;top:105px">2</span>
    <span class="num" style="left:137px;top:152px">3</span>
    <div class="item on-dark" style="left:163px;top:62px;width:85px;display:block"><h4>INSERT TITLE HERE</h4><p>Lorem ipsum sit lom dolor sit amet, consectetur sit amet. Lorem ipsum sit lom.</p></div>
    <div class="item on-dark" style="left:163px;top:109px;width:85px;display:block"><h4>INSERT TITLE HERE</h4><p>Lorem ipsum sit lom dolor sit amet, consectetur sit amet. Lorem ipsum sit lom.</p></div>
    <div class="item on-dark" style="left:163px;top:156px;width:85px;display:block"><h4>INSERT TITLE HERE</h4><p>Lorem ipsum sit lom dolor sit amet, consectetur sit amet. Lorem ipsum sit lom.</p></div>
    <div class="item" style="left:339px;top:73px;width:60px;display:block"><h4>TITLE HERE</h4><p>Lorem ipsum sit lom dolor sit amet, consectetur.</p></div>
    <div class="item on-dark" style="left:322px;top:116px;width:70px;display:block"><h4>INSERT TITLE HERE</h4><p>Lorem ipsum sit lom dolor sit amet, consectetur sit amet.</p></div>
    <div class="item" style="left:307px;top:159px;width:90px;display:block"><h4>INSERT TITLE HERE</h4><p>Lorem ipsum sit lom dolor sit amet, consectetur sit amet.</p></div>
    <div class="foot"><span></span><span></span><span>10</span></div>
  </section>

  <!-- 12 features -->
  <section class="slide" style="left:962px;top:1319px">
    <div class="pattern" style="left:200px;top:0;width:224px;height:238px" role="img" aria-label="Soft grey geometric tiles background"></div>
    <div class="mark" style="left:30px;top:27px"><i></i>BRANNOW</div>
    <div class="panel" style="left:20px;top:55px;width:382px;height:150px"></div>
    <div class="head" style="left:30px;top:107px;width:115px">
      <div class="ttl">Features slide<br>with icons</div><div class="dash"></div>
      <p class="lorem">Lorem ipsum sit lom dolor sit amet, consectetur sit amet adipiscing. Lorem ipsum sit lom dolor. Lorem ipsum.</p>
    </div>
    <div class="feat" style="left:196px;top:64px"><svg width="11" height="11"><circle cx="5.5" cy="5.5" r="4.5" fill="none" stroke="#fff" stroke-width="1.3"/><circle cx="5.5" cy="5.5" r="1.6" fill="#fff"/></svg><h4>TITLE HERE</h4><p>Sed ut perspiciatis unde omnis iste natus error</p></div>
    <div class="feat" style="left:299px;top:64px"><svg width="11" height="11"><path d="M5.5 5.5 L5.5 0.5 A5 5 0 1 1 0.5 5.5 Z" fill="#fff"/></svg><h4>TITLE HERE</h4><p>Sed ut perspiciatis unde omnis iste natus error sit</p></div>
    <div class="feat" style="left:196px;top:124px"><svg width="11" height="11"><path d="M2 1 H9 L5.5 5.5 L9 10 H2 L5.5 5.5 Z" fill="none" stroke="#fff" stroke-width="1.2"/></svg><h4>TITLE HERE</h4><p>Sed ut perspiciatis unde omnis iste natus error</p></div>
    <div class="feat" style="left:299px;top:124px"><svg width="11" height="11"><circle cx="5.5" cy="4.5" r="4" fill="#fff"/><rect x="3.5" y="8" width="4" height="2.5" fill="#fff"/></svg><h4>TITLE HERE</h4><p>Sed ut perspiciatis unde omnis iste natus error</p></div>
    <div class="foot"><span>www.brannowadvisory.com</span><span>CONFIDENTIAL</span><span>11</span></div>
  </section>

  <!-- 13 bullets with images -->
  <section class="slide" style="left:22px;top:1615px">
    <div class="panel dark" style="left:11px;width:201px"></div>
    <div class="photo" style="left:212px;top:11px;width:201px;height:216px" role="img" aria-label="Photo of a desk with a magnifying glass over printed reports and a person reading a newspaper beside a cup of tea"></div>
    <div class="mark light" style="left:30px;top:27px"><i></i>BRANNOW</div>
    <div class="ttl abs" style="left:30px;top:82px">Bullets with images</div>
    <span class="num" style="left:65px;top:107px">1</span>
    <span class="num" style="left:65px;top:136px">2</span>
    <span class="num" style="left:65px;top:165px">3</span>
    <p class="lorem abs" style="left:90px;top:108px;width:75px;text-align:left">Lorem ipsum sit lom dolor sit amet, consectetur. Lorem ipsum sit lom dolor .</p>
    <p class="lorem abs" style="left:90px;top:137px;width:75px;text-align:left">Lorem ipsum sit lom dolor sit amet, consectetur. Lorem ipsum sit lom dolor .</p>
    <p class="lorem abs" style="left:90px;top:166px;width:75px;text-align:left">Lorem ipsum sit lom dolor sit amet, consectetur. Lorem ipsum sit lom dolor .</p>
    <div class="foot"><span>www.brannowadvisory.com</span><span>CONFIDENTIAL</span><span>12</span></div>
  </section>

  <!-- 14 table + subtitle -->
  <section class="slide" style="left:492px;top:1615px">
    <div class="mark" style="left:30px;top:27px"><i></i>BRANNOW</div>
    <div class="table-head" style="left:72px;top:55px;width:185px;height:24px"><div>Columns 1</div><div>Columns 2</div></div>
    <div class="table-rows" style="left:28px;top:79px;width:44px;height:128px"><div>Rows 1</div><div>Rows 2</div></div>
    <div class="table-body" style="left:72px;top:79px;width:185px;height:128px"><div></div><div></div><div></div><div></div></div>
    <div class="panel dark" style="left:272px;width:141px"></div>
    <div class="head" style="left:293px;top:34px;width:105px">
      <div class="ttl">Title subtitle<br>+ 2 rows and<br>2 columns of<br>content (4<br>box)</div>
      <p class="lorem" style="margin-top:6px">Lorem ipsum sit lom dolor sit amet, consectetur sit amet adipiscing. Lorem ipsum sit lom dolor sit amet, consectetur adipiscing</p>
      <p class="lorem" style="margin-top:5px">Lorem ipsum sit lom dolor sit amet, consectetur sit amet adipiscing. Lorem ipsum sit lom.</p>
    </div>
    <div class="foot"><span>www.brannowadvisory.com</span><span>CONFIDENTIAL</span><span>13</span></div>
  </section>

  <!-- 15 table -->
  <section class="slide" style="left:962px;top:1615px">
    <div class="mark" style="left:30px;top:27px"><i></i>BRANNOW</div>
    <div class="abs" style="left:66px;top:27px;font-size:8px;font-weight:700;color:var(--ink)">TITLE 2 ROWS AND 2 COLUMNS OF CONTENT <span style="font-size:4px">(4 BOXES)</span></div>
    <div class="table-head" style="left:104px;top:55px;width:266px;height:24px"><div>Columns 1</div><div>Columns 2</div></div>
    <div class="table-rows" style="left:41px;top:79px;width:63px;height:128px"><div>Rows 1</div><div>Rows 2</div></div>
    <div class="table-body" style="left:104px;top:79px;width:266px;height:128px"><div></div><div></div><div></div><div></div></div>
    <div class="foot"><span>www.brannowadvisory.com</span><span>CONFIDENTIAL</span><span>14</span></div>
  </section>

  <!-- 16 nascar -->
  <section class="slide" style="left:22px;top:1912px">
    <div class="panel dark" style="left:11px;width:402px;height:94px"></div>
    <div class="mark light" style="left:30px;top:24px"><i></i>BRANNOW</div>
    <div class="ttl abs" style="left:30px;top:48px">Nascar slide with comments</div>
    <p class="lorem abs" style="left:30px;top:63px;width:360px">Lorem ipsum sit lom dolor sit amet, consectetur sit amet adipiscing. Lorem ipsum sit lom dolor. Lorem ipsum sit lom dolor sit amet, consectetur sit amet adipiscing elit. Lorem ipsum sit lom dolor sit amet, consectetur sit amet adipiscing. Lorem ipsum sit lom dolor.. Lorem ipsum sit lom dolor sit amet, consectetur sit amet adipiscing. Lorem ipsum sit lom dolor. Lorem ipsum sit lom dolor sit amet, consectetur sit amet adipiscing. Lorem ipsum sit lom dolor.</p>
    <span class="nascar a" style="left:25px;top:130px">VELTRIX</span>
    <span class="nascar b" style="left:102px;top:130px">BRANNOW</span>
    <span class="nascar a" style="left:180px;top:130px">VELTRIX</span>
    <span class="nascar b" style="left:257px;top:130px">BRANNOW</span>
    <span class="nascar a" style="left:335px;top:130px">VELTRIX</span>
    <span class="nascar b" style="left:25px;top:185px">BRANNOW</span>
    <span class="nascar a" style="left:102px;top:185px">VELTRIX</span>
    <span class="nascar b" style="left:180px;top:185px">BRANNOW</span>
    <span class="nascar a" style="left:257px;top:185px">VELTRIX</span>
    <span class="nascar b" style="left:335px;top:185px">BRANNOW</span>
    <div class="foot"><span>www.brannowadvisory.com</span><span>CONFIDENTIAL</span><span>15</span></div>
  </section>

  <!-- 17 data pie -->
  <section class="slide" style="left:492px;top:1912px">
    <div class="panel dark" style="left:11px;width:134px"></div>
    <div class="panel grey" style="left:145px;width:99px"></div>
    <div class="mark light" style="left:30px;top:27px"><i></i>BRANNOW</div>
    <div class="head" style="left:30px;top:65px;width:95px">
      <div class="ttl">Data slide</div><div class="dash"></div>
      <p class="lorem">Lorem ipsum sit lom dolor sit amet, consectetur sit amet adipiscing. Lorem ipsum sit lom dolor. Lorem ipsum.</p>
      <p class="lorem" style="margin-top:5px">Lorem ipsum sit lom dolor sit amet, consectetur sit amet adipiscing. Lorem ipsum sit lom dolor. Lorem ipsum.</p>
      <p class="lorem" style="margin-top:5px">Lorem ipsum sit lom dolor sit amet, consectetur sit amet adipiscing. Lorem ipsum sit lom dolor. Lorem ipsum.</p>
    </div>
    <div class="feat" style="left:159px;top:35px"><svg width="9" height="10"><path d="M1 1 H8 L4.5 5 L8 9 H1 L4.5 5 Z" fill="none" stroke="#fff" stroke-width="1.1"/></svg><h4>TITLE HERE</h4><p>Lorem ipsum sit lom dolor sit.</p></div>
    <div class="feat" style="left:159px;top:86px"><svg width="10" height="10"><circle cx="5" cy="5" r="4" fill="none" stroke="#fff" stroke-width="1.1"/><path d="M1 5 H9 M5 1 V9" stroke="#fff" stroke-width=".8"/></svg><h4>TITLE HERE</h4><p>Lorem ipsum sit lom dolor sit.</p></div>
    <div class="feat" style="left:159px;top:137px"><svg width="10" height="10"><circle cx="4" cy="4" r="3" fill="none" stroke="#fff" stroke-width="1.1"/><path d="M6 6 L9 9" stroke="#fff" stroke-width="1.3"/></svg><h4>TITLE HERE</h4><p>Lorem ipsum sit lom dolor sit.</p></div>
    <svg class="abs" style="left:0;top:0" width="424" height="238">
      <g stroke="#fff" stroke-width="1">
        <path d="M335 104 L335 34 A70 70 0 1 1 277.7 144.2 Z" fill="#58595c"/>
        <path d="M335 104 L277.7 144.2 A70 70 0 0 1 269.2 80.1 Z" fill="#8e8f92"/>
        <path d="M335 104 L269.2 80.1 A70 70 0 0 1 300 43.4 Z" fill="#d6d6d7"/>
        <path d="M335 104 L300 43.4 A70 70 0 0 1 335 34 Z" fill="#1f74c7"/>
      </g>
      <g font-size="3" fill="#666" font-family="Montserrat,sans-serif">
        <circle cx="291" cy="199" r="1.3" fill="#58595c"/><text x="294" y="200">1st Qtr</text>
        <circle cx="308" cy="199" r="1.3" fill="#8e8f92"/><text x="311" y="200">2nd Qtr</text>
        <circle cx="326" cy="199" r="1.3" fill="#d6d6d7"/><text x="329" y="200">3rd Qtr</text>
        <circle cx="343" cy="199" r="1.3" fill="#1f74c7"/><text x="346" y="200">4th Qtr</text>
      </g>
    </svg>
    <div class="foot"><span>www.brannowadvisory.com</span><span>CONFIDENTIAL</span><span>16</span></div>
  </section>

  <!-- 18 data bars -->
  <section class="slide" style="left:962px;top:1912px">
    <div class="panel dark" style="left:11px;width:134px"></div>
    <div class="panel grey" style="left:145px;width:68px"></div>
    <div class="mark light" style="left:30px;top:27px"><i></i>BRANNOW</div>
    <div class="head" style="left:30px;top:65px;width:95px">
      <div class="ttl">Data slide</div><div class="dash"></div>
      <p class="lorem">Lorem ipsum sit lom dolor sit amet, consectetur sit amet adipiscing. Lorem ipsum sit lom dolor. Lorem ipsum.</p>
      <p class="lorem" style="margin-top:5px">Lorem ipsum sit lom dolor sit amet, consectetur sit amet adipiscing. Lorem ipsum sit lom dolor. Lorem ipsum.</p>
      <p class="lorem" style="margin-top:5px">Lorem ipsum sit lom dolor sit amet, consectetur sit amet adipiscing. Lorem ipsum sit lom dolor. Lorem ipsum.</p>
    </div>
    <div class="feat" style="left:144px;top:35px"><svg width="9" height="10"><path d="M1 1 H8 L4.5 5 L8 9 H1 L4.5 5 Z" fill="none" stroke="#fff" stroke-width="1.1"/></svg><h4>TITLE HERE</h4><p>Lorem ipsum sit lom dolor sit.</p></div>
    <div class="feat" style="left:144px;top:86px"><svg width="10" height="10"><circle cx="5" cy="5" r="4" fill="none" stroke="#fff" stroke-width="1.1"/><path d="M1 5 H9 M5 1 V9" stroke="#fff" stroke-width=".8"/></svg><h4>TITLE HERE</h4><p>Lorem ipsum sit lom dolor sit.</p></div>
    <div class="feat" style="left:144px;top:137px"><svg width="10" height="10"><circle cx="4" cy="4" r="3" fill="none" stroke="#fff" stroke-width="1.1"/><path d="M6 6 L9 9" stroke="#fff" stroke-width="1.3"/></svg><h4>TITLE HERE</h4><p>Lorem ipsum sit lom dolor sit.</p></div>
    <svg class="abs" style="left:0;top:0" width="424" height="238">
      <text x="312" y="46" text-anchor="middle" font-size="4.5" font-weight="600" fill="#666" font-family="Montserrat,sans-serif">Chart Title</text>
      <g stroke="#eee" stroke-width=".5"><path d="M230 60 H400 M230 85 H400 M230 110 H400 M230 135 H400 M230 160 H400 M230 185 H400"/></g>
      <path d="M230 196 H400" stroke="#bbb" stroke-width=".6"/>
      <g>
        <rect x="238" y="86" width="6" height="110" fill="#1f74c7"/><rect x="245" y="134" width="6" height="62" fill="#58595c"/><rect x="252" y="141" width="6" height="55" fill="#a7a8aa"/>
        <rect x="280" y="124" width="6" height="72" fill="#1f74c7"/><rect x="287" y="84" width="6" height="112" fill="#58595c"/><rect x="294" y="134" width="6" height="62" fill="#a7a8aa"/>
        <rect x="322" y="126" width="6" height="70" fill="#1f74c7"/><rect x="329" y="148" width="6" height="48" fill="#58595c"/><rect x="336" y="104" width="6" height="92" fill="#a7a8aa"/>
        <rect x="364" y="78" width="6" height="118" fill="#1f74c7"/><rect x="371" y="128" width="6" height="68" fill="#58595c"/><rect x="378" y="68" width="6" height="128" fill="#a7a8aa"/>
      </g>
      <g font-size="2.8" fill="#777" font-family="Montserrat,sans-serif" text-anchor="middle">
        <text x="248" y="201">Category 1</text><text x="290" y="201">Category 2</text><text x="332" y="201">Category 3</text><text x="374" y="201">Category 4</text>
        <text x="311" y="206">■ Series 1  ■ Series 2  ■ Series 3</text>
      </g>
    </svg>
    <div class="foot"><span>www.brannowadvisory.com</span><span>CONFIDENTIAL</span><span>17</span></div>
  </section>

  <!-- 19 donuts -->
  <section class="slide" style="left:22px;top:2208px">
    <div class="panel dark" style="left:11px;width:123px"></div>
    <div class="mark light" style="left:30px;top:27px"><i></i>BRANNOW</div>
    <div class="head" style="left:30px;top:62px;width:90px">
      <div class="ttl">Data slide</div><div class="dash"></div>
      <p class="lorem" style="text-align:left">Lorem ipsum sit lom dolor sit amet, consectetur sit amet</p>
      <p class="lorem" style="margin-top:8px;text-align:left">Lorem ipsum sit lom dolor sit amet, consectetur sit amet.</p>
      <p class="lorem" style="margin-top:8px;text-align:left">Lorem ipsum sit lom dolor sit amet, consectetur sit amet.</p>
      <p class="lorem" style="margin-top:8px;text-align:left">Lorem ipsum sit lom dolor sit amet, consectetur sit amet.</p>
    </div>
    <svg class="abs" style="left:0;top:0" width="424" height="238" font-family="Montserrat,sans-serif">
      <g font-size="3.6" font-weight="700" fill="#1f74c7" text-anchor="middle">
        <text x="205" y="48">CHART 1</text><text x="330" y="48">CHART 2</text><text x="205" y="140">CHART 3</text><text x="330" y="140">CHART 4</text>
      </g>
      <g fill="none" stroke="#e2e2e3" stroke-width="4">
        <circle cx="205" cy="82" r="24"/><circle cx="330" cy="84" r="24"/><circle cx="205" cy="175" r="24"/><circle cx="330" cy="175" r="24"/>
      </g>
      <g fill="none" stroke="#1f74c7" stroke-width="4">
        <circle cx="205" cy="82" r="24" stroke-dasharray="30.2 150.8" transform="rotate(-90 205 82)"/>
        <circle cx="330" cy="84" r="24" stroke-dasharray="60.3 150.8" transform="rotate(-90 330 84)"/>
        <circle cx="205" cy="175" r="24" stroke-dasharray="22.6 150.8" transform="rotate(-90 205 175)"/>
        <circle cx="330" cy="175" r="24" stroke-dasharray="128.2 150.8" transform="rotate(-90 330 175)"/>
      </g>
      <g font-size="13" font-weight="600" fill="#1f74c7" text-anchor="middle">
        <text x="205" y="87">20</text><text x="330" y="89">40</text><text x="205" y="180">15</text><text x="330" y="180">85</text>
      </g>
    </svg>
    <div class="foot"><span>www.brannowadvisory.com</span><span>CONFIDENTIAL</span><span>18</span></div>
  </section>

  <!-- 20 cycle infographic -->
  <section class="slide" style="left:492px;top:2208px">
    <div class="panel dark" style="left:11px;width:123px"></div>
    <div class="mark light" style="left:30px;top:27px"><i></i>BRANNOW</div>
    <div class="head" style="left:30px;top:62px;width:90px">
      <div class="ttl">Editable<br>infographic<br>slide</div><div class="dash"></div>
      <p class="lorem">Lorem ipsum sit lom dolor sit amet, consectetur sit amet adipiscing. Lorem ipsum sit lom dolor. Lorem ipsum.</p>
      <p class="lorem" style="margin-top:5px">Lorem ipsum sit lom dolor sit amet, consectetur sit amet adipiscing. Lorem ipsum sit lom dolor. Lorem ipsum.</p>
    </div>
    <svg class="abs" style="left:0;top:0" width="424" height="238"><circle cx="285" cy="132" r="62" fill="none" stroke="#5b5e62" stroke-width="3"/></svg>
    <div class="flow" style="left:247px;top:45px;width:74px;height:35px;background:#000"><b>Lorem Ipsum</b>• Some text here<br>• Some text here</div>
    <div class="flow" style="left:180px;top:100px;width:76px;height:35px;background:var(--blue-light)"><b>Lorem Ipsum</b>• Some text here<br>• Some text here</div>
    <div class="flow" style="left:311px;top:100px;width:76px;height:35px;background:var(--slate)"><b>Lorem Ipsum</b>• Some text here<br>• Some text here</div>
    <div class="flow" style="left:205px;top:168px;width:76px;height:36px;background:var(--charcoal)"><b>Lorem Ipsum</b>• Some text here<br>• Some text here</div>
    <div class="flow" style="left:285px;top:168px;width:78px;height:36px;background:var(--blue)"><b>Lorem Ipsum</b>• Some text here<br>• Some text here</div>
    <div class="foot"><span>www.brannowadvisory.com</span><span>CONFIDENTIAL</span><span>19</span></div>
  </section>

  <!-- 21 wheel infographic -->
  <section class="slide" style="left:962px;top:2208px">
    <div class="mark" style="left:30px;top:27px"><i></i>BRANNOW</div>
    <svg class="abs" style="left:0;top:0" width="424" height="238" font-family="Montserrat,sans-serif">
      <g stroke="#fff" stroke-width="3">
        <path d="M175 148 L110.3 127 A68 68 0 0 1 175 80 Z" fill="#6b6d70"/>
        <path d="M175 148 L175 80 A68 68 0 0 1 239.7 127 Z" fill="#1f74c7"/>
        <path d="M175 148 L239.7 127 A68 68 0 0 1 215 203 Z" fill="#6b6d70"/>
        <path d="M175 148 L215 203 A68 68 0 0 1 135 203 Z" fill="#111"/>
        <path d="M175 148 L135 203 A68 68 0 0 1 110.3 127 Z" fill="#1a5aa0"/>
      </g>
      <g fill="#fff" text-anchor="middle" font-size="4.2" font-weight="700">
        <text x="151" y="114">Lorem Ipsum</text><text x="199" y="114">Lorem Ipsum</text>
        <text x="213" y="159">Lorem Ipsum</text><text x="175" y="187">Lorem Ipsum</text><text x="137" y="159">Lorem Ipsum</text>
      </g>
      <g fill="#fff" text-anchor="middle" font-size="3.2">
        <text x="151" y="119">• Some text here</text><text x="151" y="123">• Some text here</text>
        <text x="199" y="119">• Some text here</text><text x="199" y="123">• Some text here</text>
        <text x="213" y="164">• Some text here</text><text x="213" y="168">• Some text here</text>
        <text x="175" y="192">• Some text here</text><text x="175" y="196">• Some text here</text>
        <text x="137" y="164">• Some text here</text><text x="137" y="168">• Some text here</text>
      </g>
    </svg>
    <div class="panel" style="left:272px;width:141px"></div>
    <div class="head" style="left:293px;top:58px;width:105px">
      <div class="ttl">Editable<br>infographic<br>slide</div><div class="dash"></div>
      <p class="lorem">Lorem ipsum sit lom dolor sit amet, consectetur sit amet adipiscing. Lorem ipsum sit lom dolor. Lorem ipsum.</p>
      <p class="lorem" style="margin-top:5px">Lorem ipsum sit lom dolor sit amet, consectetur sit amet adipiscing. Lorem ipsum sit lom dolor. Lorem ipsum.</p>
    </div>
    <div class="foot"><span>www.brannowadvisory.com</span><span>CONFIDENTIAL</span><span>20</span></div>
  </section>

</div>
</body>
</html>
```